Label - Australian Extra Virgin Olive Oil

I'm seeking a front and back label to apply to bottles/tins of my olive oil. They will be applied to green bottles of various sizes and also white tins. The labels will have the dimensions 70 x 120mm and printed at 600dpi on adhesive labels with metalised backing. With this material, any area which is not colored on the label will show through as silver - the design may make use of this feature. There are some obligatory labeling requirements in Australia including a logo showing the proportion of Australian content, and an indication of the harvest date - the design will need to make allowance for this. Also, since the label will be used in subsequent years and on various sizes of product, I need to be able to alter this with each print run.I have a logo to use on the front label and another I would like to use on the back as this latter one will tie in with other future products (non olive oil).
The text for the back label
"Tallowby Creek is a family run enterprise. Our olives are grown on the banks of the Wendrake River in Central Victoria and processed locally
email; quietheron@pelinet.com.au
text needed for the front label design
"Australian Extra-Virgin Olive Oil"

```html
<!DOCTYPE html>
<html lang="en">
<head>
<meta charset="utf-8">
<title>Tallowby Creek – Olive Oil Labels</title>
<link rel="stylesheet" href="https://fonts.googleapis.com/css2?family=Open+Sans:wght@400;600&family=Delius&family=Alice&display=swap">
<style>
  :root {
    --backdrop: #968f8e;
    --paper-top: #e4e4e5;
    --paper-bottom: #fafafa;
    --green-light: #7bb342;
    --green-mid: #5a9a3a;
    --green-dark: #356b30;
    --frame-orange: #f5a623;
    --frame-yellow: #f4d21f;
    --brand-green: #4f7a36;
    --badge-olive: #6b7431;
    --headline: #e6e6e6;
    --body-white: #ffffff;
    --leaf-light: #a9d57f;
    --ink: #2b2b2b;
  }
  html, body {
    margin: 0;
    padding: 0;
    width: 1200px;
    height: 1200px;
    overflow: hidden;
    background: var(--backdrop);
  }
  .label-sheet { display: block; width: 1200px; height: 1200px; }
  .brand-name { font-family: "Open Sans", sans-serif; font-weight: 600; fill: var(--brand-green); text-anchor: middle; }
  .brand-name--back { font-family: "Delius", cursive; font-weight: 400; fill: var(--badge-olive); }
  .brand-mark { fill: var(--brand-green); }
  .brand-mark--back { fill: var(--badge-olive); }
  .headline { font-family: "Open Sans", sans-serif; font-weight: 400; fill: var(--headline); text-anchor: middle; }
  .story { font-family: "Delius", cursive; fill: var(--body-white); text-anchor: middle; font-size: 34px; }
  .contact { font-family: "Delius", cursive; fill: var(--body-white); font-size: 28px; }
  .field-label { font-family: "Alice", serif; fill: var(--ink); }
  .field-pill { fill: url(#pillFill); }
  .frame { fill: none; stroke: url(#frameStroke); stroke-width: 5; }
</style>
</head>
<body>
<svg class="label-sheet" viewBox="0 0 1500 1500" xmlns="http://www.w3.org/2000/svg">
  <defs>
    <linearGradient id="paperFill" x1="0" y1="0" x2="0" y2="1">
      <stop offset="0" stop-color="var(--paper-top)"/>
      <stop offset="1" stop-color="var(--paper-bottom)"/>
    </linearGradient>
    <linearGradient id="greenFill" x1="0" y1="0" x2="0" y2="1">
      <stop offset="0" stop-color="var(--green-light)"/>
      <stop offset="0.5" stop-color="var(--green-mid)"/>
      <stop offset="1" stop-color="var(--green-dark)"/>
    </linearGradient>
    <linearGradient id="frameStroke" x1="0" y1="0" x2="0" y2="1">
      <stop offset="0" stop-color="var(--frame-orange)"/>
      <stop offset="1" stop-color="var(--frame-yellow)"/>
    </linearGradient>
    <linearGradient id="pillFill" x1="0" y1="0" x2="1" y2="0">
      <stop offset="0" stop-color="#ffffff"/>
      <stop offset="1" stop-color="#e2e2e2"/>
    </linearGradient>
    <linearGradient id="foliageFill" x1="0" y1="0" x2="0" y2="1">
      <stop offset="0" stop-color="var(--leaf-light)" stop-opacity="0"/>
      <stop offset="0.35" stop-color="var(--leaf-light)" stop-opacity="0.45"/>
      <stop offset="1" stop-color="var(--green-light)" stop-opacity="0.55"/>
    </linearGradient>
    <clipPath id="frontShape">
      <polygon points="60,225 145,168 645,168 728,225 728,1255 645,1310 145,1310 60,1255"/>
    </clipPath>
    <clipPath id="backShape">
      <polygon points="773,225 858,168 1362,168 1448,225 1448,1265 1362,1320 858,1320 773,1265"/>
    </clipPath>
  </defs>

  <!-- Front label -->
  <g class="label label--front" clip-path="url(#frontShape)">
    <rect x="60" y="168" width="668" height="1142" fill="url(#greenFill)"/>
    <rect x="60" y="168" width="668" height="405" fill="url(#paperFill)"/>
    <rect class="foliage-area" x="60" y="950" width="668" height="360" fill="url(#foliageFill)"
          role="img" aria-label="Olive leaves and branch sweeping up from the lower corners"/>
  </g>
  <polygon class="frame" points="85,235 155,188 635,188 705,235 705,1245 635,1292 155,1292 85,1245"/>

  <circle class="brand-mark" cx="395" cy="340" r="62"/>
  <text class="brand-name" x="395" y="488" font-size="72">Tallowby Creek</text>

  <text class="headline" x="396" y="720" font-size="76">AUSTRALIAN</text>
  <text class="headline" x="395" y="800" font-size="62">EXTRA VIRGIN</text>
  <text class="headline" x="397" y="903" font-size="114">OLIVE</text>
  <text class="headline" x="400" y="1005" font-size="114">OIL</text>

  <rect class="field-pill" x="263" y="1185" width="270" height="55" rx="27"/>
  <text class="field-label" x="287" y="1230" font-size="42">Vol.</text>

  <!-- Back label -->
  <g class="label label--back" clip-path="url(#backShape)">
    <rect x="773" y="168" width="675" height="1152" fill="url(#greenFill)"/>
    <polygon points="773,168 1448,168 1448,578 1290,578 1110,635 930,578 773,578" fill="url(#paperFill)"/>
  </g>
  <polygon class="frame" points="798,235 868,188 1352,188 1422,235 1422,1255 1352,1300 868,1300 798,1255"/>

  <circle class="brand-mark brand-mark--back" cx="1110" cy="320" r="62"/>
  <text class="brand-name brand-name--back" x="1110" y="470" font-size="76">Tallowby Creek</text>

  <text class="story">
    <tspan x="1110" y="712">Tallowby Creek is a family run</tspan>
    <tspan x="1110" y="765">enterprise. Our olives are grown</tspan>
    <tspan x="1110" y="818">on the banks of the Wendrake</tspan>
    <tspan x="1110" y="871">River in Central Victoria and</tspan>
    <tspan x="1110" y="924">processed locally</tspan>
  </text>

  <g class="mail-icon" fill="none" stroke="var(--body-white)" stroke-width="3">
    <rect x="943" y="1010" width="34" height="22" rx="2"/>
    <polyline points="943,1012 960,1024 977,1012"/>
    <rect x="950" y="999" width="20" height="14" fill="var(--green-mid)"/>
  </g>
  <text class="contact" x="993" y="1028">quietheron@pelinet.com.au</text>

  <g class="content-badge">
    <rect x="876" y="1120" width="95" height="137" fill="#ffffff" stroke="#2f8a6b" stroke-width="2"/>
    <rect x="888" y="1132" width="71" height="76" fill="#1f8a6a"/>
    <rect x="888" y="1213" width="71" height="32" fill="#f3b22a"/>
  </g>

  <rect class="field-pill" x="997" y="1167" width="378" height="42" rx="21"/>
  <text class="field-label" x="1009" y="1196" font-size="24">Havest date:</text>
</svg>
</body>
</html>
```